Create a new business card

I’m looking to update my business card to make it match the rest of my brand. I will include my current website as well as what my vehicle designs look like, etc..
What my business currently services
Weekly maintenance pool openings / closings
Equipment repair, including pumps, heaters, salt systems, filters, etc.
We install automatic covers and maintain them as well as provide preventative maintenance

I would like to include my name.
Darren Holcott.
My title
Owner
My email
Darren@tidewellnx.com
4015867120
Www.tidewellnx.com

```html
<!DOCTYPE html>
<html lang="en">
<head>
<meta charset="utf-8">
<title>Tidewell Pool Service – Business Card</title>
<link rel="stylesheet" href="https://fonts.googleapis.com/css2?family=Montserrat:wght@400;500;700&display=swap">
<style>
  :root {
    --navy: #232f63;
    --sky: #3db4e8;
    --mid: #2a6fb0;
    --white: #ffffff;
    --backdrop: #c4c4c4;
  }
  * { box-sizing: border-box; margin: 0; padding: 0; }
  html, body { width: 1200px; height: 900px; overflow: hidden; }
  body {
    background: var(--backdrop);
    font-family: "Montserrat", sans-serif;
    position: relative;
  }
  .card {
    position: absolute;
    left: 320px;
    width: 560px;
    height: 320px;
    border-radius: 16px;
    overflow: hidden;
  }
  .card--front { top: 100px; background: var(--white); }
  .card--back {
    top: 480px;
    background: linear-gradient(20deg, var(--sky) 0%, #2f8fcc 40%, var(--mid) 65%, var(--navy) 100%);
    color: var(--white);
  }
  .wave { position: absolute; inset: 0; width: 100%; height: 100%; }

  .brand {
    position: absolute;
    display: flex;
    align-items: center;
    gap: 12px;
    font-weight: 700;
    line-height: 1.15;
  }
  .brand__dot { width: 34px; height: 34px; border-radius: 50%; flex: none; }
  .card--front .brand { left: 34px; top: 128px; color: var(--navy); font-size: 22px; }
  .card--front .brand__dot { background: var(--sky); }
  .card--back .brand { left: 34px; top: 122px; color: var(--white); font-size: 24px; }
  .card--back .brand__dot { background: var(--white); }

  .divider { position: absolute; width: 1.5px; }
  .card--front .divider { left: 236px; top: 96px; height: 128px; background: var(--navy); }
  .card--back .divider { left: 262px; top: 80px; height: 160px; background: rgba(255,255,255,.75); }

  .contact { position: absolute; left: 258px; top: 96px; color: var(--navy); }
  .contact__name { font-size: 22px; font-weight: 700; letter-spacing: .3px; }
  .contact__title { font-size: 12px; font-weight: 400; margin-bottom: 14px; }
  .contact__list { list-style: none; font-size: 12px; }
  .contact__list li { display: flex; align-items: center; gap: 8px; margin-bottom: 6px; }
  .contact__list svg { width: 12px; height: 12px; fill: var(--sky); flex: none; }

  .services { position: absolute; left: 284px; top: 78px; }
  .services__title { color: var(--sky); font-size: 22px; font-weight: 700; margin-bottom: 8px; }
  .services__list { list-style: none; font-size: 13px; line-height: 1.75; }
  .services__list li::before { content: "•"; margin-right: 8px; }
</style>
</head>
<body>

  <section class="card card--front">
    <svg class="wave" viewBox="0 0 560 320" preserveAspectRatio="none" aria-hidden="true">
      <path d="M470 0 C540 60 520 220 390 320 L560 320 L560 0 Z" fill="var(--sky)"/>
      <path d="M486 0 C556 70 540 230 410 320 L560 320 L560 0 Z" fill="var(--white)"/>
      <path d="M498 0 C566 80 556 236 430 320 L560 320 L560 0 Z" fill="var(--navy)"/>
    </svg>
    <div class="brand"><span class="brand__dot"></span><span>Tidewell<br>Pool Service</span></div>
    <div class="divider"></div>
    <div class="contact">
      <h1 class="contact__name">Darren Holcott</h1>
      <p class="contact__title">Owner</p>
      <ul class="contact__list">
        <li><svg viewBox="0 0 24 24"><path d="M6.6 10.8a15 15 0 0 0 6.6 6.6l2.2-2.2a1 1 0 0 1 1-.25 11.4 11.4 0 0 0 3.6.57 1 1 0 0 1 1 1V20a1 1 0 0 1-1 1A17 17 0 0 1 3 4a1 1 0 0 1 1-1h3.5a1 1 0 0 1 1 1c0 1.25.2 2.45.57 3.57a1 1 0 0 1-.25 1z"/></svg>4015867120</li>
        <li><svg viewBox="0 0 24 24"><path d="M2 5h20v14H2z M2 5l10 8 10-8" /></svg>Darren@tidewellnx.com</li>
        <li><svg viewBox="0 0 24 24"><circle cx="12" cy="12" r="10"/></svg>Www.tidewellnx.com</li>
      </ul>
    </div>
  </section>

  <section class="card card--back">
    <div class="brand"><span class="brand__dot"></span><span>Tidewell<br>Pool Service</span></div>
    <div class="divider"></div>
    <div class="services">
      <h2 class="services__title">OUR SERVICES</h2>
      <ul class="services__list">
        <li>Pool Opening and Closing</li>
        <li>Renovation</li>
        <li>Weekly pool services</li>
        <li>Electronoc Lake detection</li>
        <li>Structural Pool Repair</li>
        <li>Equipment repairs andUpgrades</li>
      </ul>
    </div>
  </section>

</body>
</html>
```